Icons design for a GPS application

You have to provide a professional design with 30 icons (See attachment [url removed, login to view] [url removed, login to view] [url removed, login to view]) and a dashboard that will be put in a GPS app.
The dashboard must be original and could be similar to attachment [url removed, login to view] and [url removed, login to view]
The work must be made in Photoshop and the psd file with all layers and effects should be present.
The size for the icons must be 512x512px.
The dashboard have design for vertical / horizontal devices at minimum 1280px.

Please send a dashboard with at least 6 icons on it first (for winning the contest, and the rest afterwards):
- GPS position
- Menu
- Layers
- Compass
- zoom in
- zoom out
It could be something similar to [url removed, login to view] but the layout and colors are your choice.

```html
<!DOCTYPE html>
<html lang="en">
<head>
<meta charset="utf-8">
<title>GPS Dashboard</title>
<link href="https://fonts.googleapis.com/css2?family=Oswald:wght@500&family=Arimo:wght@400;700&display=swap" rel="stylesheet">
<style>
  :root {
    --bg: #d5d5d7;
    --tile: #5b5b5d;
    --halo: #b4b4b6;
    --band: #5a5a5c;
    --gap: #c9c9cb;
    --segment: #4b4b4d;
    --hub: #7b7b7d;
    --bar-side: #8a8a8c;
    --bar-mid: #a9a9ab;
    --ink: #ffffff;
  }
  html, body { margin: 0; padding: 0; overflow: hidden; background: var(--bg); }
  .dashboard { width: 1200px; height: 792px; display: block; }
  .tile { fill: var(--tile); }
  .halo { fill: var(--halo); }
  .band { fill: var(--band); }
  .gap { fill: var(--gap); }
  .segment-field { fill: var(--segment); }
  .spoke { stroke: var(--gap); stroke-width: 9; }
  .hub { fill: var(--hub); }
  .bar-side { fill: var(--bar-side); }
  .bar-mid { fill: var(--bar-mid); }
  .icon { fill: var(--ink); }
  .icon-line { fill: none; stroke: var(--ink); stroke-linecap: round; stroke-linejoin: round; }
  .app-name { font-family: 'Oswald', sans-serif; font-weight: 500; font-size: 47px; fill: var(--ink); }
  .location { font-family: 'Arimo', sans-serif; font-size: 17px; fill: var(--ink); }
  .menu-label { font-family: 'Arimo', sans-serif; font-weight: 700; font-size: 31px; fill: var(--ink); }
  .bar-title { font-family: 'Arimo', sans-serif; font-size: 29px; fill: var(--ink); }
</style>
</head>
<body>
<svg class="dashboard" viewBox="0 0 1200 792" xmlns="http://www.w3.org/2000/svg">
  <!-- corner tiles -->
  <rect class="tile" x="24" y="24" width="296" height="272"/>
  <rect class="tile" x="880" y="24" width="296" height="272"/>
  <rect class="tile" x="24" y="496" width="296" height="197"/>
  <rect class="tile" x="880" y="496" width="296" height="197"/>

  <!-- dial -->
  <ellipse class="halo" cx="600" cy="376" rx="488" ry="318"/>
  <ellipse class="band" cx="600" cy="376" rx="452" ry="290"/>
  <ellipse class="gap" cx="600" cy="376" rx="441" ry="281"/>
  <ellipse class="segment-field" cx="600" cy="376" rx="432" ry="273"/>
  <g class="spokes">
    <line class="spoke" x1="600" y1="376" x2="1045" y2="376"/>
    <line class="spoke" x1="600" y1="376" x2="985" y2="518"/>
    <line class="spoke" x1="600" y1="376" x2="822" y2="622"/>
    <line class="spoke" x1="600" y1="376" x2="600" y2="660"/>
    <line class="spoke" x1="600" y1="376" x2="378" y2="622"/>
    <line class="spoke" x1="600" y1="376" x2="215" y2="518"/>
    <line class="spoke" x1="600" y1="376" x2="155" y2="376"/>
    <line class="spoke" x1="600" y1="376" x2="215" y2="234"/>
    <line class="spoke" x1="600" y1="376" x2="378" y2="130"/>
    <line class="spoke" x1="600" y1="376" x2="600" y2="92"/>
    <line class="spoke" x1="600" y1="376" x2="822" y2="130"/>
    <line class="spoke" x1="600" y1="376" x2="985" y2="234"/>
  </g>
  <ellipse class="gap" cx="600" cy="376" rx="216" ry="106"/>
  <ellipse class="hub" cx="600" cy="376" rx="206" ry="97"/>
  <text class="app-name" x="600" y="392" text-anchor="middle">GPS APPS NAME</text>
  <text class="location" x="600" y="416" text-anchor="middle">Current Location: New York</text>

  <!-- traffic light -->
  <g class="icon-set" transform="translate(518 173)">
    <rect class="icon" x="-13" y="-28" width="26" height="56" rx="6"/>
    <rect class="icon" x="-21" y="-22" width="10" height="6" rx="2"/>
    <rect class="icon" x="11" y="-22" width="10" height="6" rx="2"/>
    <rect class="icon" x="-21" y="-3" width="10" height="6" rx="2"/>
    <rect class="icon" x="11" y="-3" width="10" height="6" rx="2"/>
    <rect class="icon" x="-21" y="16" width="10" height="6" rx="2"/>
    <rect class="icon" x="11" y="16" width="10" height="6" rx="2"/>
    <circle cx="0" cy="-17" r="5.5" fill="var(--segment)"/>
    <circle cx="0" cy="0" r="5.5" fill="var(--segment)"/>
    <circle cx="0" cy="17" r="5.5" fill="var(--segment)"/>
  </g>

  <!-- layers -->
  <g transform="translate(682 173)">
    <path class="icon" d="M0 -28 L32 -14 L0 0 L-32 -14 Z"/>
    <path class="icon" d="M-32 -2 L-22 -6 L0 4 L22 -6 L32 -2 L0 12 Z"/>
    <path class="icon" d="M-32 10 L-22 6 L0 16 L22 6 L32 10 L0 24 Z"/>
  </g>

  <!-- locate target -->
  <g transform="translate(823 228)">
    <circle class="icon-line" r="20" stroke-width="5"/>
    <circle class="icon" r="10"/>
    <path class="icon-line" stroke-width="5" d="M0 -32 V-20 M0 20 V32 M-32 0 H-20 M20 0 H32"/>
  </g>

  <!-- zoom in -->
  <g transform="translate(904 318)">
    <circle class="icon-line" cx="-6" cy="-6" r="18" stroke-width="4.5"/>
    <path class="icon-line" stroke-width="4.5" d="M-15 -6 H3 M-6 -15 V3"/>
    <path class="icon-line" stroke-width="9" d="M9 9 L24 24"/>
  </g>

  <!-- zoom out -->
  <g transform="translate(904 432)">
    <circle class="icon-line" cx="-6" cy="-6" r="18" stroke-width="4.5"/>
    <path class="icon-line" stroke-width="4.5" d="M-15 -6 H3"/>
    <path class="icon-line" stroke-width="9" d="M9 9 L24 24"/>
  </g>

  <!-- airport pin -->
  <g transform="translate(682 565)">
    <path class="icon" d="M0 44 L-20 10 A24 24 0 1 1 20 10 Z"/>
    <path fill="var(--segment)" d="M-2 -18 Q0 -22 2 -18 V-6 L14 2 V6 L2 1 V10 L6 14 V16 L0 14 L-6 16 V14 L-2 10 V1 L-14 6 V2 L-2 -6 Z"/>
  </g>

  <!-- park pin -->
  <g transform="translate(518 565)">
    <path class="icon" d="M0 44 L-20 10 A24 24 0 1 1 20 10 Z"/>
    <path fill="var(--segment)" d="M0 -20 L8 -8 H4 L11 2 H6 L13 12 H-13 L-6 2 H-11 L-4 -8 H-8 Z"/>
    <rect fill="var(--segment)" x="-2" y="12" width="4" height="6"/>
  </g>

  <!-- folded map -->
  <g transform="translate(361 526)">
    <path class="icon-line" stroke-width="4.5" d="M-24 -18 L-8 -24 L8 -18 L24 -24 V18 L8 24 L-8 18 L-24 24 Z M-8 -24 V18 M8 -18 V24"/>
  </g>

  <!-- flag -->
  <g transform="translate(292 434)">
    <rect class="icon" x="-22" y="-26" width="5" height="54"/>
    <path class="icon" d="M-17 -24 Q-4 -30 6 -22 Q16 -14 26 -20 V6 Q16 12 6 4 Q-4 -4 -17 2 Z"/>
  </g>

  <!-- hiker -->
  <g transform="translate(286 314)">
    <circle class="icon" cx="2" cy="-28" r="6"/>
    <rect class="icon" x="-16" y="-18" width="10" height="20" rx="3"/>
    <path class="icon-line" stroke-width="8" d="M0 -16 V6 M0 6 L-8 28 M0 6 L8 28"/>
    <path class="icon-line" stroke-width="4" d="M2 -12 L12 -2 M16 -6 V30"/>
  </g>

  <!-- settings gear -->
  <g transform="translate(361 218)">
    <circle class="icon" r="17"/>
    <g class="icon">
      <rect x="-5" y="-25" width="10" height="50" rx="1"/>
      <rect x="-5" y="-25" width="10" height="50" rx="1" transform="rotate(45)"/>
      <rect x="-5" y="-25" width="10" height="50" rx="1" transform="rotate(90)"/>
      <rect x="-5" y="-25" width="10" height="50" rx="1" transform="rotate(135)"/>
    </g>
    <circle r="7" fill="var(--segment)"/>
  </g>

  <!-- globe -->
  <g transform="translate(117 109)" class="icon-line" stroke-width="4">
    <circle r="36"/>
    <ellipse rx="15" ry="36"/>
    <path d="M0 -36 V36 M-36 0 H36 M-31 -18 H31 M-31 18 H31"/>
  </g>

  <!-- share -->
  <g transform="translate(1084 109)">
    <path class="icon-line" stroke-width="5" d="M-22 0 L22 -24 M-22 0 L22 24"/>
    <circle class="icon" cx="-22" cy="0" r="13"/>
    <circle class="icon" cx="22" cy="-24" r="13"/>
    <circle class="icon" cx="22" cy="24" r="13"/>
  </g>

  <!-- home -->
  <g transform="translate(117 618)">
    <path class="icon" d="M-42 0 L0 -38 L42 0 L36 6 L0 -26 L-36 6 Z"/>
    <rect class="icon" x="20" y="-34" width="9" height="20"/>
    <path class="icon" d="M-28 4 L0 -20 L28 4 V36 H8 V14 H-8 V36 H-28 Z"/>
  </g>

  <!-- satellite dish -->
  <g transform="translate(1098 616)">
    <path class="icon" d="M-34 -26 A34 34 0 0 0 14 22 Z"/>
    <path class="icon-line" stroke-width="5" d="M-10 -2 L8 -20"/>
    <circle class="icon" cx="10" cy="-22" r="5"/>
    <path class="icon-line" stroke-width="4" d="M16 -34 A14 14 0 0 1 24 -22 M20 -46 A26 26 0 0 1 36 -24"/>
    <path class="icon-line" stroke-width="5" d="M-10 6 L-26 40 M-10 6 L2 40"/>
  </g>

  <!-- bottom bar -->
  <rect class="bar-side" x="24" y="706" width="296" height="65"/>
  <rect class="bar-mid" x="320" y="706" width="560" height="65"/>
  <rect class="bar-side" x="880" y="706" width="296" height="65"/>
  <text class="menu-label" x="172" y="749" text-anchor="middle">Menu</text>
  <text class="bar-title" x="600" y="748" text-anchor="middle">GPS Dashboard</text>
  <text class="menu-label" x="1028" y="749" text-anchor="middle">Menu</text>
</svg>
</body>
</html>
```